Podcast Cover Art Design for Divorce Support

Need a podcast cover art design for new podcast that will cover Emotional Divorce Support and Recovery topics. People are lost, confused. They are looking for help during the confusion and heartbreak. Main Title is "Quiet Harbor Podcast". Subtitle is "How to Let Go and Move On". We want a design that is encouraging yet not overly "happy". We also want to convey kindness, clarity, and strength, if possible. Our logo colors use grey and red though we aren't tied to those colors for the podcast. Logo may be used on the podcast but not required. Final image should be 3000x3000px. Our logo uses Montserrat-Medium and Multi-SemiBold. Not necessary but available if you want to use it.

```html
<!DOCTYPE html>
<html lang="en">
<head>
<meta charset="utf-8">
<title>Quiet Harbor Podcast — Cover Art</title>
<link rel="stylesheet" href="https://fonts.googleapis.com/css2?family=Montserrat:wght@400;800&display=swap">
<style>
  :root {
    --brand-red: #e41d25;
    --brand-grey: #7b7b7b;
    --paper: #ffffff;
    --paper-edge: #dedede;
    --photo-blue: #9aaec4;
    --photo-blue-deep: #5f7690;
    --photo-amber: #eaa94c;
    --photo-red: #c8322c;
    --photo-green: #3f8a3a;
    --photo-shadow: #2c2a2e;
  }
  * { margin: 0; padding: 0; box-sizing: border-box; }
  html, body {
    width: 1200px;
    height: 1200px;
    overflow: hidden;
    background: var(--paper);
  }
  .cover {
    position: relative;
    width: 1200px;
    height: 1200px;
    background: var(--paper);
    overflow: hidden;
  }
  .cover-photo {
    position: absolute;
    left: 0;
    top: 410px;
    width: 1200px;
    height: 790px;
    background:
      radial-gradient(ellipse 38% 30% at 58% 48%, rgba(255, 226, 170, 0.55) 0%, rgba(255, 226, 170, 0) 100%),
      radial-gradient(ellipse 60% 40% at 50% 110%, rgba(44, 42, 46, 0.55) 0%, rgba(44, 42, 46, 0) 100%),
      linear-gradient(to bottom, rgba(0,0,0,0) 78%, rgba(63,138,58,0.55) 100%),
      linear-gradient(115deg,
        var(--photo-blue-deep) 0%,
        var(--photo-blue) 22%,
        #b7c3d0 34%,
        var(--photo-amber) 46%,
        #d98a46 56%,
        var(--photo-red) 70%,
        #b52a25 82%,
        #d8dde3 100%);
  }
  .torn-edge {
    position: absolute;
    left: 0;
    top: 388px;
    width: 1200px;
    height: 110px;
  }
  .title-block {
    position: absolute;
    left: 0;
    top: 0;
    width: 1200px;
    height: 380px;
  }
  .title-line {
    font-family: "Montserrat", sans-serif;
    font-weight: 800;
  }
  .title-line--primary { fill: var(--brand-red); font-size: 150px; }
  .title-line--secondary { fill: var(--brand-grey); font-size: 90px; }
  .title-tag {
    font-family: "Montserrat", sans-serif;
    font-weight: 400;
    font-size: 37px;
    fill: var(--brand-red);
  }
  .subtitle-bar { fill: var(--brand-grey); }
  .subtitle-text {
    font-family: "Montserrat", sans-serif;
    font-weight: 400;
    font-size: 40px;
    fill: var(--paper);
  }
</style>
</head>
<body>
  <main class="cover">
    <div class="cover-photo" role="img" aria-label="Photograph of a support group seated in a circle outdoors, stacking their hands together in the middle"></div>

    <svg class="torn-edge" viewBox="0 0 1200 110" width="1200" height="110" aria-hidden="true">
      <path fill="var(--paper-edge)" d="M0 0 H1200 V18 L1170 34 L1140 30 L1110 52 L1080 44 L1040 40 L1000 52 L965 48 L935 44 L900 60 L860 52 L820 54 L790 62 L760 56 L730 54 L700 66 L670 58 L640 50 L610 62 L580 50 L550 54 L520 56 L480 48 L450 40 L420 52 L390 40 L360 58 L330 64 L300 52 L270 38 L245 18 L220 36 L200 32 L175 44 L150 52 L120 46 L90 56 L60 54 L30 44 L0 40 Z"/>
      <path fill="var(--paper)" d="M0 0 H1200 V8 L1170 24 L1140 20 L1110 42 L1080 34 L1040 30 L1000 42 L965 38 L935 34 L900 50 L860 42 L820 44 L790 52 L760 46 L730 44 L700 56 L670 48 L640 40 L610 52 L580 40 L550 44 L520 46 L480 38 L450 30 L420 42 L390 30 L360 48 L330 54 L300 42 L270 28 L245 8 L220 26 L200 22 L175 34 L150 42 L120 36 L90 46 L60 44 L30 34 L0 30 Z"/>
    </svg>

    <svg class="title-block" viewBox="0 0 1200 380" width="1200" height="380" role="img" aria-label="Quiet Harbor Podcast — How to let go and move on">
      <text class="title-line title-line--primary" x="245" y="183" textLength="705" lengthAdjust="spacingAndGlyphs">QUIET</text>
      <text class="title-line title-line--secondary" x="245" y="268" textLength="452" lengthAdjust="spacingAndGlyphs">HARBOR</text>
      <text class="title-tag" x="708" y="249" textLength="240" lengthAdjust="spacing">PODCAST</text>
      <rect class="subtitle-bar" x="245" y="288" width="705" height="65"/>
      <text class="subtitle-text" x="290" y="335" textLength="611" lengthAdjust="spacingAndGlyphs">HOW TO LET GO AND MOVE ON</text>
    </svg>
  </main>
</body>
</html>
```